Corvane Electrical Solutions

On one side. LOGO (underneath:) Commercial Industrial Residential

- NAME & CONTACT DETAILS

Marcus T. Hollings
Project Manager

(Cell icon) (441) 582-6197
(Email icon) cvnelectricalsoultions@mailventra.com
(Facebook & Instagram icons )@cvnelectricalsolutions

Other side: LOGO - underneath ELECTRICAL CONSTRUCTION & MAINTENANCE . LED LIGHTING & AUTOMATION . LIFE SAFETY SYSTEMS (FIRE ALARM / SECURITY) . DATA & COMMUNICATION

```html
<!DOCTYPE html>
<html lang="en">
<head>
<meta charset="utf-8">
<title>Corvane Electrical Solutions – Business Cards</title>
<link rel="stylesheet" href="https://fonts.googleapis.com/css2?family=Montserrat:wght@400;500;600;700&family=Arimo:wght@400&display=swap">
<style>
  :root {
    --teal: #15566e;
    --slate: #4a4a4a;
    --paper: #ffffff;
    --backdrop: #d6d6d3;
    --ink: #333333;
  }
  * { margin: 0; padding: 0; box-sizing: border-box; }
  html, body { width: 1200px; height: 801px; overflow: hidden; }
  body {
    background: var(--backdrop);
    position: relative;
    font-family: "Arimo", Arial, sans-serif;
  }
  .card {
    position: absolute;
    top: 250px;
    width: 520px;
    height: 300px;
    background: var(--paper);
    box-shadow: 0 6px 18px rgba(0,0,0,0.18);
    overflow: hidden;
  }
  .card--contact { left: 60px; }
  .card--services { left: 620px; }

  /* wordmark */
  .wordmark {
    display: flex;
    align-items: center;
    gap: 12px;
  }
  .wordmark__mark {
    width: 26px; height: 26px;
    background: var(--teal);
    flex: none;
  }
  .wordmark__name {
    font-family: "Montserrat", sans-serif;
    font-weight: 600;
    color: var(--teal);
    text-transform: uppercase;
    letter-spacing: 0.14em;
    line-height: 1.15;
  }

  /* contact side */
  .card--contact .wordmark { position: absolute; left: 40px; top: 70px; }
  .card--contact .wordmark__name { font-size: 13px; }
  .identity { position: absolute; left: 40px; top: 180px; }
  .identity__name {
    font-family: "Montserrat", sans-serif;
    font-weight: 700;
    font-size: 22px;
    color: var(--teal);
  }
  .identity__role {
    font-size: 13px;
    color: var(--ink);
    margin-top: 4px;
  }
  .contact {
    position: absolute;
    left: 272px;
    top: 90px;
    padding-left: 16px;
    border-left: 1.5px solid var(--teal);
    list-style: none;
  }
  .contact__item {
    display: flex;
    align-items: center;
    gap: 7px;
    font-size: 11.5px;
    color: var(--ink);
    line-height: 1;
    margin: 7px 0;
  }
  .contact__icon { width: 11px; height: 11px; flex: none; }
  .contact__dot {
    width: 10px; height: 10px;
    border-radius: 50%;
    background: var(--teal);
    flex: none;
  }

  /* services side */
  .card--services .wordmark {
    position: absolute;
    left: 0; right: 0; top: 70px;
    justify-content: center;
  }
  .card--services .wordmark__mark { width: 34px; height: 34px; }
  .card--services .wordmark__name { font-size: 18px; }
  .services-band {
    position: absolute;
    left: 0; right: 0; bottom: 0;
    height: 100px;
    background: var(--teal);
    border-top: 5px solid var(--slate);
    display: grid;
    grid-template-columns: 300px 1fr;
    align-content: center;
    row-gap: 12px;
    padding: 0 18px;
    list-style: none;
  }
  .services-band__item {
    color: var(--paper);
    font-size: 10.5px;
    letter-spacing: 0.03em;
    text-transform: uppercase;
    white-space: nowrap;
    display: flex;
    align-items: center;
    gap: 7px;
  }
  .services-band__item::before {
    content: "";
    width: 6px; height: 6px;
    border: 1px solid var(--paper);
    border-radius: 50%;
    flex: none;
  }
</style>
</head>
<body>

<section class="card card--contact">
  <div class="wordmark">
    <span class="wordmark__mark"></span>
    <span class="wordmark__name">Corvane<br>Electrical<br>Solutions</span>
  </div>
  <div class="identity">
    <p class="identity__name">Marcus T. Hollings</p>
    <p class="identity__role">Project Manager</p>
  </div>
  <ul class="contact">
    <li class="contact__item">
      <svg class="contact__icon" viewBox="0 0 24 24" aria-hidden="true"><path fill="#15566e" d="M6.6 10.8a15.1 15.1 0 0 0 6.6 6.6l2.2-2.2c.3-.3.7-.4 1-.2 1.1.4 2.3.6 3.6.6.6 0 1 .4 1 1V20c0 .6-.4 1-1 1C10.6 21 3 13.4 3 4c0-.6.4-1 1-1h3.5c.6 0 1 .4 1 1 0 1.3.2 2.5.6 3.6.1.3 0 .7-.2 1z"/></svg>
      (441) 582-6197
    </li>
    <li class="contact__item">
      <svg class="contact__icon" viewBox="0 0 24 24" aria-hidden="true"><rect x="2" y="5" width="20" height="14" fill="#15566e"/><path d="M2 5l10 8 10-8" fill="none" stroke="#fff" stroke-width="1.6"/></svg>
      cvnelectricalsoultions@mailventra.com
    </li>
    <li class="contact__item"><span class="contact__dot"></span>@cvnelectricalsolutions</li>
    <li class="contact__item"><span class="contact__dot"></span>@cvnelectricalsolutions</li>
  </ul>
</section>

<section class="card card--services">
  <div class="wordmark">
    <span class="wordmark__mark"></span>
    <span class="wordmark__name">Corvane<br>Electrical<br>Solutions</span>
  </div>
  <ul class="services-band">
    <li class="services-band__item">Electrical Construction &amp; Maintenance</li>
    <li class="services-band__item">LED Lighting &amp; Automation</li>
    <li class="services-band__item">Life Safety Systems (Fire Alarm / Security)</li>
    <li class="services-band__item">Data &amp; Communication</li>
  </ul>
</section>

</body>
</html>
```